Criação de Papelaria Profissional para Consultoria de Negócios
A empresa queria:
" Serviços de Consultoria de Carreira (transição, desenvolvimento de liderança), Assessment, Coaching, Outplacement, Headhunting "

```html
<!DOCTYPE html>
<html lang="pt-BR">
<head>
<meta charset="UTF-8">
<title>Marina Tessari – Papel Timbrado</title>
<link href="https://fonts.googleapis.com/css2?family=Open+Sans:wght@400;600&display=swap" rel="stylesheet">
<style>
  :root {
    --backdrop: #ecebe8;
    --paper: #ffffff;
    --wine: #6b1a24;
    --ink: #3a3a3a;
    --muted: #8a8a8a;
    --faint: #efefef;
  }
  * { margin: 0; padding: 0; box-sizing: border-box; }
  html, body { width: 1200px; height: 1200px; overflow: hidden; }
  body {
    background: var(--backdrop);
    font-family: "Open Sans", Arial, sans-serif;
    color: var(--ink);
  }
  .letterhead {
    position: absolute;
    left: 210px; top: 34px;
    width: 780px; height: 1132px;
    background: var(--paper);
    box-shadow: 0 6px 24px rgba(0,0,0,0.12);
    overflow: hidden;
  }
  .brand {
    position: absolute;
    right: 70px; top: 70px;
    text-align: right;
  }
  .brand-line { display: flex; align-items: center; justify-content: flex-end; gap: 12px; }
  .brand-dot { width: 18px; height: 18px; border-radius: 50%; background: var(--wine); }
  .brand-name {
    font-size: 28px; font-weight: 400; letter-spacing: 3px;
    text-transform: uppercase; color: var(--wine);
  }
  .brand-tagline {
    margin-top: 4px;
    font-size: 10px; letter-spacing: 3px; text-transform: uppercase; color: var(--muted);
  }
  .letter-body {
    position: absolute;
    left: 70px; top: 220px; width: 640px;
    font-size: 14px; line-height: 1.75; color: var(--ink);
  }
  .letter-body p { margin-bottom: 18px; text-align: justify; }
  .contact-list {
    position: absolute;
    left: 70px; bottom: 170px;
    list-style: none;
    font-size: 12px; color: var(--muted);
  }
  .contact-list li { display: flex; align-items: center; gap: 10px; margin-bottom: 8px; }
  .contact-icon {
    width: 20px; height: 20px; border-radius: 50%; background: var(--wine);
    display: flex; align-items: center; justify-content: center; flex-shrink: 0;
  }
  .sign-off {
    position: absolute;
    left: 330px; bottom: 110px;
    font-size: 12px; color: var(--muted);
  }
  .signature {
    width: 150px; height: 48px; margin: 10px 0 6px;
    background: linear-gradient(90deg, rgba(120,120,120,0.08), rgba(120,120,120,0.22), rgba(120,120,120,0.08));
    border-radius: 24px;
  }
  .signer-name { color: var(--ink); font-size: 12px; }
  .signer-role { font-size: 11px; }
  .footer-band {
    position: absolute; left: 0; right: 0; bottom: 0;
    height: 16px; background: var(--wine);
  }
</style>
</head>
<body>
  <main class="letterhead">
    <header class="brand">
      <div class="brand-line">
        <span class="brand-dot"></span>
        <span class="brand-name">Marina Tessari</span>
      </div>
      <div class="brand-tagline">Consultoria de Carreira</div>
    </header>

    <section class="letter-body">
      <p>Prezado cliente, agradecemos a confiança depositada em nossa equipe. Este documento apresenta a proposta de acompanhamento para a transição de carreira, com etapas claras, metas objetivas e encontros mensais de avaliação do progresso alcançado.</p>
      <p>O programa inclui assessment de competências, sessões individuais de coaching e apoio na construção de um plano de desenvolvimento de liderança. Cada fase será conduzida por consultores experientes, sempre alinhados aos objetivos da sua organização e ao perfil de cada profissional envolvido.</p>
      <p>Ficamos à disposição para esclarecer dúvidas e ajustar o cronograma conforme a sua necessidade.</p>
    </section>

    <ul class="contact-list">
      <li>
        <span class="contact-icon"><svg width="11" height="11" viewBox="0 0 24 24"><path fill="#fff" d="M6.6 10.8a15 15 0 0 0 6.6 6.6l2.2-2.2a1 1 0 0 1 1-.25 11.4 11.4 0 0 0 3.6.57 1 1 0 0 1 1 1V20a1 1 0 0 1-1 1A17 17 0 0 1 3 4a1 1 0 0 1 1-1h3.5a1 1 0 0 1 1 1c0 1.25.2 2.45.57 3.6a1 1 0 0 1-.25 1z"/></svg></span>
        (11) 4321-7788
      </li>
      <li>
        <span class="contact-icon"><svg width="11" height="11" viewBox="0 0 24 24"><rect x="3" y="6" width="18" height="12" rx="1" fill="none" stroke="#fff" stroke-width="2"/><path d="M3 7l9 6 9-6" fill="none" stroke="#fff" stroke-width="2"/></svg></span>
        contato@marinatessari.com.br
      </li>
      <li>
        <span class="contact-icon"><svg width="11" height="11" viewBox="0 0 24 24"><circle cx="12" cy="12" r="9" fill="none" stroke="#fff" stroke-width="2"/><path d="M3 12h18M12 3c3 3 3 15 0 18M12 3c-3 3-3 15 0 18" fill="none" stroke="#fff" stroke-width="1.6"/></svg></span>
        www.marinatessari.com.br
      </li>
      <li>
        <span class="contact-icon"><svg width="11" height="11" viewBox="0 0 24 24"><path fill="#fff" d="M12 2a7 7 0 0 0-7 7c0 5 7 13 7 13s7-8 7-13a7 7 0 0 0-7-7zm0 9.5A2.5 2.5 0 1 1 12 6.5a2.5 2.5 0 0 1 0 5z"/></svg></span>
        Rua das Acácias, 245 – São Paulo, SP
      </li>
    </ul>

    <div class="sign-off">
      <div>Atenciosamente,</div>
      <div class="signature" role="img" aria-label="Assinatura manuscrita"></div>
      <div class="signer-name">Paulo Reis</div>
      <div class="signer-role">Diretor</div>
    </div>

    <div class="footer-band"></div>
  </main>
</body>
</html>
```